Pruett Design & Millwork needs a web presence. Looking for a unique Design so please submit an idea.

In brief, you should know the following about me: My company was established in 2001 and had been responsible for providing reasonable CAD Design and Custom Millwork ever since. My specialty is in the area Architectural CAD Design, Fabrication of Custom Millwork and Mouldings on a partime basis. Drawings and estimates done at a very reasonable cost. I look forward to working on your next project. Thanks in Advance, Glen 
I would like one page to show thumbnails linked to some of past millwork projects and another page with thumbnails linking to some of my house designs. I assume last page will have contact information accessed from a link on home page. I already had a logo designed which I can supply you with to design home page around. As I indicated I have a regular full time job and do this for additional income and will move to full time when I have enough business.

I have attached the logo I had designed in a couple different colors. I have also uploaded some PDF's of files that I also considered before choosing the RED LOGO to give an ideas of how we could tweak the logo to better fit the website if need be. Text is wrong in those.

Thanks,
Glen

I added my logo as a PDF side there seems to be a problem with scaling loge with the other file. Hope this helps.

Glen

Evening,
I will be hosting this site on servquill. Its looks like it will get launched with wordpress?  What will be involved from getting your design up so I can upload project pictures and and text to areas you have set aside? I am also going to upload a couple jpg of a couple recent projects so you can put in so I can get a feel of what they will look like. Thanks for all your work to date! Glen

I am not seeing alot of design variations or even many designers in fact. Is there something more from me you need? Do you need me to extend deadline?

Reason: It appears that your need some more time to submit some design changes. I will choose a design next week after changes have been submitted. Thanks for your time. Glen

Reason: Designers needs a couple days to submit some last minute changes. Thanks for all your submissions! Glen

Reason: Some last minute designs that I need to look at and give feedback on. I want to thank everyone for their designs and patience. Thanks again, Glen

Evening All,

Upon discussion with a couple of the designers I want the design done in Word Press and I have increased budget the amount they said they would need to do it for. Thanks for all submissions so far but I am still looking for the special one that stands out among the rest! Glen

I will not be extending deadline and choosing designer tomorrow morning so if you have anything else to add please do so tonight. Thanks for all your submissions. Glen

Target Market(s)

Millwork projects will be generally local where as CAD Design Projects could be emailed anywhere. Probably more USA but who knows.

Industry/Entity Type

House

Font styles to use
Other font styles liked:
• Eras Medium ITC, Calibri or Designers choice.

Requirements
Must have
• Must tie in my logo on Homepage at least. Could even be somewhat transparent in background? I will let the designer work that out.
Nice to have
• Page to point to current and past Design projects on one page and millwork on another.
Should not have
• Target a large Corporate or Global environment since it is a small business right now.

```html
<!DOCTYPE html>
<html lang="en">
<head>
<meta charset="utf-8">
<title>Pruett Design &amp; Millwork</title>
<link rel="stylesheet" href="https://fonts.googleapis.com/css2?family=Questrial&family=Open+Sans:wght@400&display=swap">
<style>
  :root {
    --page-bg: #ffffff;
    --sky-light: #e9f0f3;
    --sky-mid: #b9cdd6;
    --sky-deep: #6f93a2;
    --nav-bg: rgba(52, 74, 84, 0.92);
    --nav-home: #1d2c34;
    --panel-bg: rgba(62, 86, 96, 0.88);
    --header-dark: #333333;
    --section-bg: rgba(255, 255, 255, 0.72);
    --section-border: #c9c9c9;
    --thumb-border: #9a9a9a;
    --plan-fill: #f4f4f4;
    --text-light: #ffffff;
    --text-soft: #d7e0e4;
    --brand-ink: #1f2a30;
  }
  * { margin: 0; padding: 0; box-sizing: border-box; }
  html, body { width: 1200px; height: 997px; overflow: hidden; background: var(--page-bg); }
  .canvas { position: relative; width: 1200px; height: 997px; overflow: hidden; font-family: "Open Sans", sans-serif; }

  .backdrop {
    position: absolute; inset: 0;
    background:
      radial-gradient(ellipse 420px 520px at 640px 260px, var(--sky-mid) 0%, rgba(185,205,214,0.35) 55%, rgba(255,255,255,0) 100%),
      radial-gradient(ellipse 360px 260px at 620px 960px, rgba(111,147,162,0.45) 0%, rgba(255,255,255,0) 100%),
      linear-gradient(180deg, var(--sky-light) 0%, #ffffff 60%, #f1f4f6 100%);
  }

  .brand { position: absolute; left: 24px; top: 150px; width: 200px; display: flex; align-items: center; gap: 10px; }
  .brand-mark { width: 22px; height: 22px; background: var(--brand-ink); flex: none; }
  .brand-name { font-family: "Questrial", sans-serif; font-size: 20px; line-height: 1.15; color: var(--brand-ink); }

  .main-nav { position: absolute; left: 277px; top: 116px; width: 894px; height: 43px; background: var(--nav-bg); display: flex; align-items: center; }
  .nav-home { width: 72px; height: 43px; background: var(--nav-home); display: flex; align-items: center; justify-content: center; }
  .nav-link { position: absolute; top: 0; height: 43px; line-height: 43px; font-family: "Questrial", sans-serif; font-size: 23px; color: var(--text-light); text-decoration: none; transform: translateX(-50%); white-space: nowrap; }

  .welcome { position: absolute; left: 277px; top: 159px; width: 894px; height: 172px; background: var(--panel-bg); padding: 26px 30px 0 27px; }
  .welcome-title { font-family: "Questrial", sans-serif; font-weight: 400; font-size: 30px; color: var(--text-light); margin-bottom: 12px; }
  .welcome-text { font-size: 16.5px; line-height: 21px; color: var(--text-soft); }

  .showcase { position: absolute; left: 277px; width: 894px; background: var(--section-bg); border: 1px solid var(--section-border); }
  .showcase--millwork { top: 359px; height: 242px; }
  .showcase--houses { top: 629px; height: 241px; }
  .showcase-title { height: 44px; line-height: 44px; background: var(--header-dark); color: var(--text-light); font-family: "Questrial", sans-serif; font-size: 17px; text-transform: uppercase; padding-left: 19px; }
  .thumb { position: absolute; width: 187px; height: 142px; border: 1px solid var(--thumb-border); }
  .thumb--plan { background: var(--plan-fill); }
  .thumb--house { background: linear-gradient(180deg, #6f8fb0 0%, #8a8a86 45%, #6b6a5e 70%, #3f5a2c 100%); }
</style>
</head>
<body>
<div class="canvas">
  <div class="backdrop" role="img" aria-label="Architectural wireframe sketch of a modern glass building against a pale sky"></div>

  <div class="brand">
    <span class="brand-mark"></span>
    <span class="brand-name">Pruett Design &amp; Millwork</span>
  </div>

  <nav class="main-nav">
    <a class="nav-home" href="#" aria-label="Home">
      <svg width="22" height="19" viewBox="0 0 22 19"><path d="M11 1 L1 10 H4 V18 H9 V12 H13 V18 H18 V10 H21 Z" fill="#ffffff"/></svg>
    </a>
    <a class="nav-link" href="#" style="left:143px">about</a>
    <a class="nav-link" href="#" style="left:346px">millwork projects</a>
    <a class="nav-link" href="#" style="left:594px">house designs</a>
    <a class="nav-link" href="#" style="left:809px">contact us</a>
  </nav>

  <section class="welcome">
    <h1 class="welcome-title">Welcome to Pruett Design &amp; Milwork</h1>
    <p class="welcome-text">Ut wisi enim ad minim veniam, quis nostrud exerci tation ullamcorper suscipit lobortis nisl ut aliquip ex ea commodo consequat. Duis autem vel eum iriure dolor in hendrerit in vulputate velit esse molestie consequat, vel illum dolore eu feugiat nulla facilisis a</p>
  </section>

  <section class="showcase showcase--millwork">
    <h2 class="showcase-title">Recent Millwork Projects</h2>
    <div class="thumb thumb--plan" style="left:29px;top:67px" role="img" aria-label="Floor plan drawing of a millwork project"></div>
    <div class="thumb thumb--plan" style="left:244px;top:67px" role="img" aria-label="Floor plan drawing of a millwork project"></div>
    <div class="thumb thumb--plan" style="left:459px;top:67px" role="img" aria-label="Floor plan drawing of a millwork project"></div>
    <div class="thumb thumb--plan" style="left:674px;top:67px" role="img" aria-label="Floor plan drawing of a millwork project"></div>
  </section>

  <section class="showcase showcase--houses">
    <h2 class="showcase-title">Recent House Designs</h2>
    <div class="thumb thumb--house" style="left:29px;top:64px" role="img" aria-label="3D rendering of a dark two-storey house with a deck"></div>
    <div class="thumb thumb--house" style="left:244px;top:64px" role="img" aria-label="3D rendering of a grey two-storey house"></div>
    <div class="thumb thumb--house" style="left:459px;top:64px" role="img" aria-label="3D rendering of a yellow log-style house"></div>
    <div class="thumb thumb--house" style="left:674px;top:64px" role="img" aria-label="3D rendering of a beige house with a wraparound porch"></div>
  </section>
</div>
</body>
</html>
```